Website redesign for Halt and reBloom

We would like to update the design of our current website to a more concise, conversion optimized design.
The goal of our website is to get our message across as concisely as possible plus encourage people to contact us for more information or to book a consultation.
We need a redesign of the home page and 1 internal page - just for design/layout purposes/format purposes.

Target Market(s)

Males 20-45 years old who are concerned about hair loss and who want to regrow their own hair.

Industry/Entity Type

Health And Wellness

Number of Pages Required

2 page

Font styles to use
Sans Serif

Colors
00a990
33a6d7
ffffff
9d9d9d

Requirements
Must have
• We want the home page to be very concise and to the point in getting the message across. We want to get across the following 6 key messages:
• 1. Dr Quimby story – why he created this solution
• 2. Hair loss is caused by a chemical imbalance
• 3. Halt and rebloom conducts genetic and DNA analysis, then rebalances body chemistry, thus reversing the hair loss process and enabling your own hair to regrow naturally
• 4. Money back guaranteed results
• 5. Only The Active ingredients – no harsh preservatives or chemicals are included
• 6. All ingredients are FDA approved and safe – no side effects
• We also need a strong call to action. We want people to call or email us to find out more information or to schedule a consultation.
• Here is our current website which is not performing as we would hope: http://www.haltandrebloom-example.com/
• Here is our press release for further information: https://www.pressdeskly-example.com/news/finally-we-now-have-a-cure-for-male-pattern-baldness-19187647
• I uploaded the logo files, but let me know if anything else is needed and I can add it.

```html
<!DOCTYPE html>
<html lang="en">
<head>
<meta charset="utf-8">
<title>Halt &amp; reBloom – Home</title>
<link href="https://fonts.googleapis.com/css2?family=Jost:wght@300;400;500;600&family=Open+Sans:wght@400;600;700&display=swap" rel="stylesheet">
<style>
:root{
  --teal:#00a990;
  --teal-dark:#008f7a;
  --blue:#33a6d7;
  --white:#ffffff;
  --grey:#9d9d9d;
  --text:#4a4a4a;
  --light:#f0f0f0;
  --ink:#222;
}
*{box-sizing:border-box;margin:0;padding:0}
html,body{width:1200px;height:2740px;overflow:hidden}
body{font-family:"Open Sans",Arial,sans-serif;color:var(--text);background:var(--white)}
.container{width:1000px;margin:0 auto;position:relative}

/* header */
.site-header{height:137px;background:var(--white)}
.site-header .container{height:137px;display:flex;align-items:center;justify-content:space-between}
.brand{display:flex;align-items:center;gap:14px}
.brand-mark{width:56px;height:56px;border-radius:50%;background:var(--teal)}
.brand-text{font-family:"Jost",sans-serif;font-weight:400;color:var(--teal);line-height:1.1}
.brand-name{font-size:36px;display:block}
.brand-sub{font-size:22px;display:block;padding-left:110px}
.header-right{display:flex;align-items:center;gap:56px}
.phone{font-family:"Jost",sans-serif;font-size:25px;color:var(--teal);display:flex;align-items:center;gap:10px}
.lang{width:154px;height:38px;border:1px solid #ddd;font-size:12px;color:#777;display:flex;align-items:center;gap:10px;padding:0 14px}
.lang .flag{width:22px;height:14px;background:#3b4a8c}
.lang .caret{margin-left:auto}

/* nav */
.main-nav{height:55px;background:var(--teal)}
.main-nav ul{list-style:none;display:flex;height:55px;width:1000px;margin:0 auto}
.main-nav li{font-family:"Jost",sans-serif;font-size:14px;color:var(--white);text-transform:uppercase;padding:0 20px;display:flex;align-items:center}
.main-nav li.active{background:var(--teal-dark)}

/* hero */
.hero{position:relative;height:568px;background:linear-gradient(160deg,#5a5d63 0%,#8a8380 40%,#c9a896 60%,#77726f 100%);overflow:hidden}
.hero-title{position:absolute;top:196px;left:0;right:0;text-align:center;font-family:"Jost",sans-serif;font-weight:300;font-size:38px;letter-spacing:3px;line-height:48px;color:var(--white);text-transform:uppercase}
.hero-play{position:absolute;left:564px;top:290px}
.hero-arrow{position:absolute;top:230px;width:44px;height:44px;border-radius:50%;background:rgba(255,255,255,.18)}
.hero-arrow.prev{left:22px}.hero-arrow.next{right:22px}
.hero-wave{position:absolute;bottom:0;left:0}

/* welcome */
.welcome{height:503px;background:var(--blue);color:var(--white);padding-top:66px}
.welcome h1{font-family:"Jost",sans-serif;font-weight:400;font-size:33px;text-align:center;letter-spacing:1px}
.welcome .intro{width:930px;margin:18px auto 0;font-size:11px;line-height:18px;text-align:center}
.checklist{list-style:none;width:660px;margin:26px 0 0 310px}
.checklist li{font-size:15px;line-height:21px;margin-bottom:16px;display:flex;gap:12px}
.checklist svg{flex:none;margin-top:1px}

/* story */
.story{height:532px;padding-top:90px}
.story .container{display:flex;justify-content:space-between}
.story-copy{width:540px}
.story-copy h2{font-size:15px;font-weight:700;line-height:24px;color:#555}
.story-copy p{font-size:11px;line-height:22px;color:#888;margin-top:16px}
.btn{display:inline-block;background:var(--teal);color:var(--white);font-family:"Jost",sans-serif;font-size:16px;text-transform:uppercase;padding:0 30px;height:44px;line-height:44px}
.story-copy .btn{margin-top:36px}
.story-figure{width:372px;height:356px;border:1px solid #ddd;padding:8px;background:var(--white)}
.story-figure .fill{width:100%;height:100%;background:linear-gradient(180deg,#eef1ec 0%,#9cb07f 45%,#6c7d52 70%,#eceee9 100%)}

/* features */
.features{height:601px;background:var(--light);padding-top:78px}
.features .container{display:flex;justify-content:space-between}
.feature{width:290px;text-align:center}
.feature-photo{width:214px;height:214px;border-radius:50%;border:4px solid #3bb5a0;margin:0 auto}
.feature:nth-child(1) .feature-photo{background:linear-gradient(160deg,#c5d4cf,#5a9f8c 60%,#3e3a38)}
.feature:nth-child(2) .feature-photo{background:linear-gradient(160deg,#eee,#d9b9a5 50%,#e06c6c)}
.feature:nth-child(3) .feature-photo{background:linear-gradient(160deg,#f1f1f1,#d0a489 50%,#fafafa)}
.feature h3{font-family:"Open Sans",sans-serif;font-weight:700;font-size:14px;color:var(--ink);margin-top:26px;text-transform:uppercase}
.feature p{font-size:11px;line-height:20px;color:#555;margin-top:12px;height:88px}
.feature .btn{margin-top:22px;width:150px;padding:0}

/* footer */
.site-footer{height:345px;background:var(--teal);color:var(--white)}
.footer-cols{display:flex;padding-top:40px;height:276px;border-bottom:1px solid rgba(255,255,255,.35)}
.footer-col{border-right:1px solid rgba(255,255,255,.25)}
.footer-col:last-child{border:none}
.footer-col.hours{width:310px}
.footer-col.address{width:364px;padding-left:0}
.footer-col.news{flex:1;padding-left:30px}
.footer-col h4{font-family:"Jost",sans-serif;font-weight:400;font-size:17px;text-transform:uppercase;margin-bottom:18px}
.footer-col p{font-size:12px;line-height:30px;color:#e2f5f1}
.footer-col .mark{width:70px;height:70px;border-radius:50%;background:rgba(255,255,255,.55);margin-top:22px}
.signup{display:flex;margin-top:16px}
.signup .field{width:220px;height:38px;background:var(--white);color:#aaa;font-size:11px;line-height:38px;padding-left:22px}
.signup .submit{width:106px;height:38px;background:var(--teal-dark);font-size:13px;font-weight:600;line-height:38px;text-align:center}
.social{display:flex;gap:12px;margin-top:16px}
.social span{width:36px;height:36px;border-radius:50%;background:var(--white)}
.copyright{font-size:11px;color:#e2f5f1;padding-top:24px}
</style>
</head>
<body>

<header class="site-header">
  <div class="container">
    <div class="brand">
      <span class="brand-mark"></span>
      <span class="brand-text"><span class="brand-name">Halt &amp; reBloom</span><span class="brand-sub">by Harold Quimby M.D.</span></span>
    </div>
    <div class="header-right">
      <div class="phone">
        <svg width="20" height="20" viewBox="0 0 24 24"><path fill="#00a990" d="M6.6 10.8a15.1 15.1 0 0 0 6.6 6.6l2.2-2.2c.3-.3.7-.4 1-.2 1.1.4 2.3.6 3.6.6.6 0 1 .4 1 1V20c0 .6-.4 1-1 1A17 17 0 0 1 3 4c0-.6.4-1 1-1h3.5c.6 0 1 .4 1 1 0 1.3.2 2.5.6 3.6.1.3 0 .7-.2 1z"/></svg>
        Call Us: (555) 014-2290
      </div>
      <div class="lang"><span class="flag"></span>ENGLISH<span class="caret">⌄</span></div>
    </div>
  </div>
</header>

<nav class="main-nav">
  <ul>
    <li class="active">Home</li><li>About Us</li><li>How It Works</li><li>Success Stories</li><li>FAQs</li><li>Blog</li><li>Salon Partners</li><li>Book Now</li><li>Contact</li>
  </ul>
</nav>

<section class="hero" role="img" aria-label="Close-up photo of a man's thinning crown with a finger pointing at the scalp">
  <span class="hero-arrow prev"></span><span class="hero-arrow next"></span>
  <h2 class="hero-title">Stop hereditary hair loss and regrow a full<br>healthy head of hair</h2>
  <svg class="hero-play" width="72" height="72" viewBox="0 0 72 72"><circle cx="36" cy="36" r="33" fill="none" stroke="rgba(255,255,255,.6)" stroke-width="3"/><path d="M28 22 L52 36 L28 50 Z" fill="rgba(255,255,255,.6)"/></svg>
  <svg class="hero-wave" width="1200" height="40" viewBox="0 0 1200 40"><path d="M0 18 Q300 0 600 22 T1200 16 V40 H0 Z" fill="#33a6d7"/></svg>
</section>

<section class="welcome">
  <h1>WELCOME TO HALT &amp; REBLOOM</h1>
  <p class="intro">Dr. Harold Quimby is a renowned hair restoration expert and was even a contributor in the development of the Advanced High Density MICROscopic single hair transplant procedure. As a practicing derma-surgeon, he also pioneered the non-surgical rhinoplasty and has a special interest in the field of developing non-surgical solutions.</p>
  <ul class="checklist">
    <li><svg width="18" height="18" viewBox="0 0 18 18"><circle cx="9" cy="9" r="9" fill="#fff"/><path d="M5 9.3l2.6 2.6L13 6.5" fill="none" stroke="#33a6d7" stroke-width="2"/></svg>Dr Quimby story – why he created this solution</li>
    <li><svg width="18" height="18" viewBox="0 0 18 18"><circle cx="9" cy="9" r="9" fill="#fff"/><path d="M5 9.3l2.6 2.6L13 6.5" fill="none" stroke="#33a6d7" stroke-width="2"/></svg>Hair loss is caused by a chemical imbalance</li>
    <li><svg width="18" height="18" viewBox="0 0 18 18"><circle cx="9" cy="9" r="9" fill="#fff"/><path d="M5 9.3l2.6 2.6L13 6.5" fill="none" stroke="#33a6d7" stroke-width="2"/></svg>Halt and rebloom conducts genetic and DNA analysis, then rebalances body chemistry, thus reversing the hair loss process and enabling your own hair to regrow naturally</li>
    <li><svg width="18" height="18" viewBox="0 0 18 18"><circle cx="9" cy="9" r="9" fill="#fff"/><path d="M5 9.3l2.6 2.6L13 6.5" fill="none" stroke="#33a6d7" stroke-width="2"/></svg>Money back guaranteed results</li>
    <li><svg width="18" height="18" viewBox="0 0 18 18"><circle cx="9" cy="9" r="9" fill="#fff"/><path d="M5 9.3l2.6 2.6L13 6.5" fill="none" stroke="#33a6d7" stroke-width="2"/></svg>Only The Active ingredients – no harsh preservatives or chemicals are included</li>
    <li><svg width="18" height="18" viewBox="0 0 18 18"><circle cx="9" cy="9" r="9" fill="#fff"/><path d="M5 9.3l2.6 2.6L13 6.5" fill="none" stroke="#33a6d7" stroke-width="2"/></svg>All ingredients are FDA approved and safe – no side effects</li>
  </ul>
</section>

<section class="story">
  <div class="container">
    <div class="story-copy">
      <h2>The Revolutionary New Solution For Hair Loss That Uses Personalized Medicine To Stop Hair Loss and Regrow Your Thinning / Receding Hair.</h2>
      <p>Dr. Harold Quimby, the creator of Halt and reBloom is a renowned hair restoration expert. After seeing first his father and then older brothers thin and go bald, he dedicated his life to finding the cure for hair loss. After initially pioneering the single hair method for hair transplant, he determined there must be a non-surgical solution and spent the last 20 years in research and clinical trial and error first creating, then perfecting what is now the Halt and reBloom solution for hair loss.</p>
      <p>To the right you can see the Quimby family tree, or at least the five Quimby brothers from oldest to youngest. Unluckily for the oldest three Dr Quimby did not discover the cure until it was too late for them. As you can see both Harold and his younger brother (Harold is the second youngest) sport a full head of hair despite both now being well beyond the age when their older brothers had already lost their hair.</p>
      <a class="btn">Read More</a>
    </div>
    <figure class="story-figure"><div class="fill" role="img" aria-label="Illustration of a family tree with portrait photos of five brothers placed on its branches"></div></figure>
  </div>
</section>

<section class="features">
  <div class="container">
    <article class="feature">
      <div class="feature-photo" role="img" aria-label="Photo of a stylist working on a client's hair in a salon"></div>
      <h3>Why is Halt and Rebloom unique?</h3>
      <p>Halt and reBloom uses a scientific approach to hair loss by treating your unique cause. Every case is different and may include multiple causes. Unless we are treating yours, the treatment won't work for you.</p>
      <a class="btn">Read More</a>
    </article>
    <article class="feature">
      <div class="feature-photo" role="img" aria-label="Photo of a woman holding a blister pack of pills"></div>
      <h3>Personalized Medicine</h3>
      <p>Halt and reBloom uses FDA approved ingredients in a proprietary formula using individual dosages based on your personal biology and genetics. Our solution is formulated in our specialty compounding pharmacy.</p>
      <a class="btn">Read More</a>
    </article>
    <article class="feature">
      <div class="feature-photo" role="img" aria-label="Photo of a thoughtful man with a receding hairline"></div>
      <h3>Holistic Approach</h3>
      <p>While many cases of hair loss are caused by a hormone imbalance (DHT), stress and diet can cause hair loss too. Your treatment will be multi-faceted to ensure your hair loss is stopped and we regrow your hair as quickly as possible.</p>
      <a class="btn">Read More</a>
    </article>
  </div>
</section>

<footer class="site-footer">
  <div class="container">
    <div class="footer-cols">
      <div class="footer-col hours">
        <h4>Hours of Operation</h4>
        <p>Monday - Friday: 9.00am to 5.00pm</p>
        <p>Saturday: 8.00am to 2.00pm</p>
        <div class="mark"></div>
      </div>
      <div class="footer-col address" style="padding-left:40px">
        <h4>Contact Address</h4>
        <p>Halt and Rebloom Hair, LLC 1200 Fernhill Ave, Suite<br>300 Larkmont CA 90000</p>
        <p>
          <svg width="12" height="12" viewBox="0 0 24 24"><path fill="#fff" d="M6.6 10.8a15.1 15.1 0 0 0 6.6 6.6l2.2-2.2c.3-.3.7-.4 1-.2 1.1.4 2.3.6 3.6.6.6 0 1 .4 1 1V20c0 .6-.4 1-1 1A17 17 0 0 1 3 4c0-.6.4-1 1-1h3.5c.6 0 1 .4 1 1 0 1.3.2 2.5.6 3.6.1.3 0 .7-.2 1z"/></svg>
          (555) 014-2290</p>
        <p>
          <svg width="12" height="10" viewBox="0 0 24 18"><rect width="24" height="18" rx="2" fill="#fff"/><path d="M1 2l11 8 11-8" fill="none" stroke="#00a990" stroke-width="2"/></svg>
          info@haltandrebloom-example.com</p>
      </div>
      <div class="footer-col news">
        <h4>Sign up for newsletters</h4>
        <p style="line-height:18px">Please sign up here for latest news</p>
        <div class="signup"><span class="field">EMAIL ADDRESS</span><span class="submit">SUBSCRIBE</span></div>
        <div class="social"><span></span><span></span><span></span><span></span></div>
      </div>
    </div>
    <p class="copyright">© 2017 HALT &amp; REBLOOM SOLUTION. All right reserved . Term of Use</p>
  </div>
</footer>

</body>
</html>
```